Business cards and stationary for zombie fantasy camp
The Bramble Lodge
Business cards and stationary for zombie fantasy camp - Outdoors
Creative Brief
Simple
Dwight Palmer
2648 Wendel Rd Marrowfield Vt 05921
Dwight@thebramblelodge.example
www.thebramblelodge.example
Please refer to the website to get ideas as to what to add to this business card. I would like a design that speaks to the nature of the business. I have also uploaded 4 different logo's that I use, please feel free to experiment with each one. I'm in need of business cards, stationary, presentation folders, etc...
Please refer to the website to get ideas as to what to add to this business card. I would like a design that speaks to the nature of the business.
Tovick88 Tovick88
Attention please all designers: I've extended this contest for 3 days, not so much to find new designs but many of you have submitted designs that are nearing what I'm looking for. And the three days will enable us all time to communicate and work through those changes. I don't want any of you missing out because I didn't get online until only the final hours risking being able to give you all a chance to make those modifications I'm looking for. Sorry for the delay, But, thank you for your patience and all of your work.
All designers please note, you each that have submitted ideas have some excellent business card ideas, There is only 1 day left, please stop concentrating on business cards, and start focusing on stationary, letterheads, envelopes, and email signatures, I'm looking for the whole package here.
Just a quick message to thank everyone for the work that they have put into my project, I've got some excellent designs. With that being said, I still would like to see more designs for items specifically with Presentation Folders, Stationary, envelopes, and email signatures
Feel free to use any logo that I have uploaded here. I like all of them, so I look forward to seeing what you can do with any one of them or all of them.
My project had started once before, quillhaven had noticed that I had a logo project running at the same time, so they made the recommendation to put this on hold until that project finished. To the designers that submitted already, I apologize to you all. The logo project is now finished, I had multiple logo's I likes so I've posted them here for you to use as your inspiration. Good luck to you all and with all projects, I look forward to seeing your work.
I will be looking to use these designs when ordering business cards through prenta nook.example, I'm also looking for designs for stationary, envelopes and presentation folders all ordered through prentanook.example

```html
<!DOCTYPE html>
<html lang="en">
<head>
<meta charset="utf-8">
<title>The Bramble Lodge – Business Card</title>
<link href="https://fonts.googleapis.com/css2?family=Open+Sans:wght@400;600;700&display=swap" rel="stylesheet">
<style>
  :root {
    --bg: #e9e7e3;
    --orange: #f0a52a;
    --orange-deep: #d98a17;
    --black: #121212;
    --charcoal: #2e2e2e;
    --white: #ffffff;
    --label: #555555;
  }
  * { margin: 0; padding: 0; box-sizing: border-box; }
  html, body { width: 1200px; height: 398px; overflow: hidden; }
  body {
    background: var(--bg);
    font-family: "Open Sans", Arial, sans-serif;
    position: relative;
  }
  .card {
    position: absolute;
    top: 88px;
    width: 530px;
    height: 252px;
    background: var(--orange);
    overflow: hidden;
    box-shadow: 0 2px 6px rgba(0,0,0,.25);
  }
  .card--front { left: 40px; }
  .card--back { left: 624px; }
  .card__bg { position: absolute; inset: 0; }
  .contact {
    position: absolute;
    left: 28px;
    top: 62px;
    color: var(--white);
  }
  .contact__name { font-size: 17px; font-weight: 600; margin-bottom: 10px; }
  .contact__address { font-size: 10.5px; line-height: 1.45; margin-bottom: 26px; }
  .contact__list { list-style: none; }
  .contact__item {
    display: flex; align-items: center; gap: 8px;
    font-size: 10.5px; margin-bottom: 9px;
  }
  .contact__icon { width: 16px; height: 16px; flex: none; }
  .brand {
    position: absolute;
    width: 170px; height: 170px;
    border-radius: 50%;
    background: var(--black);
    display: flex; align-items: center; justify-content: center;
    text-align: center;
  }
  .card--front .brand { left: 318px; top: 41px; }
  .card--back .brand { left: 180px; top: 41px; }
  .brand__name {
    color: var(--orange);
    font-weight: 700;
    font-size: 17px;
    line-height: 1.2;
    text-transform: uppercase;
    letter-spacing: 1px;
  }
  .back-rule {
    position: absolute; top: 0; bottom: 0; width: 3px;
    background: var(--charcoal);
  }
  .back-rule--left { left: 26px; }
  .back-rule--right { right: 26px; }
  .caption {
    position: absolute; top: 356px;
    font-size: 10px; color: var(--label);
    letter-spacing: .5px;
  }
  .caption--front { left: 44px; }
  .caption--back { left: 1080px; }
</style>
</head>
<body>
  <section class="card card--front" aria-label="Front of card">
    <svg class="card__bg" viewBox="0 0 530 252" preserveAspectRatio="none">
      <defs>
        <linearGradient id="panelShade" x1="0" y1="0" x2="1" y2="0">
          <stop offset="0" stop-color="#2a2a2a"/>
          <stop offset="1" stop-color="#080808"/>
        </linearGradient>
      </defs>
      <path d="M0 0 H330 Q270 60 272 126 Q270 192 330 252 H0 Z" fill="url(#panelShade)"/>
      <path d="M330 0 H348 Q290 60 292 126 Q290 192 348 252 H330 Q270 192 272 126 Q270 60 330 0 Z" fill="var(--orange-deep)"/>
    </svg>
    <div class="contact">
      <p class="contact__name">Dwight Palmer</p>
      <p class="contact__address">2648 Wendel Rd<br>Marrowfield Vt 05921</p>
      <ul class="contact__list">
        <li class="contact__item">
          <svg class="contact__icon" viewBox="0 0 16 16"><circle cx="8" cy="8" r="8" fill="var(--orange)"/><path d="M5.5 4h1.6l.7 2-1 .8a6 6 0 0 0 2.4 2.4l.8-1 2 .7v1.6c0 .5-.4.9-.9.9A7 7 0 0 1 4.6 4.9c0-.5.4-.9.9-.9z" fill="var(--black)"/></svg>
          555-203-0147
        </li>
        <li class="contact__item">
          <svg class="contact__icon" viewBox="0 0 16 16"><circle cx="8" cy="8" r="8" fill="var(--orange)"/><rect x="4" y="5.2" width="8" height="5.6" fill="none" stroke="var(--black)" stroke-width="1.1"/><path d="M4 5.4 8 8.5l4-3.1" fill="none" stroke="var(--black)" stroke-width="1.1"/></svg>
          Dwight@thebramblelodge.example
        </li>
        <li class="contact__item">
          <svg class="contact__icon" viewBox="0 0 16 16"><circle cx="8" cy="8" r="8" fill="var(--orange)"/><circle cx="8" cy="8" r="4.2" fill="none" stroke="var(--black)" stroke-width="1"/><path d="M3.8 8h8.4M8 3.8c-2 2.4-2 6 0 8.4M8 3.8c2 2.4 2 6 0 8.4" fill="none" stroke="var(--black)" stroke-width="1"/></svg>
          www.thebramblelodge.example
        </li>
      </ul>
    </div>
    <div class="brand"><span class="brand__name">The Bramble<br>Lodge</span></div>
  </section>

  <section class="card card--back" aria-label="Back of card">
    <span class="back-rule back-rule--left"></span>
    <span class="back-rule back-rule--right"></span>
    <div class="brand"><span class="brand__name">The Bramble<br>Lodge</span></div>
  </section>

  <p class="caption caption--front">FRONT CARD</p>
  <p class="caption caption--back">BACK CARD</p>
</body>
</html>
```